Fence Flyer to Attract More Sales During Winter

We need a new flyer made that we can distribute to residential mailboxes. The flyer is to promote our Frostline Picket Days. We like simply designs, and we would like the flyer to showcase a lot of our fence photos. More of our photos are online at our website at www.getbramblerail.com - our new address needs to also be featured on the flyer - 436 Quillen rd, Monroe, NC 28117. I do want the words "FROSTLINE PICKET DAYS" to be dominate on the flyer with the description "Wood fences starting at $12/FT!" Please look through our Facebook page and our website to gather more photos or information. We are flexible on colors, nothing to fancy - simple flyer design please.

Target Market(s)

Residential homeowners that need a new fence to enclose their yard for safety, security or decorative

Industry/Entity Type

Residential Construction

Font styles to use
Sans Serif

Colors

Designer to choose colors to be used in the design.

Requirements
Must have
• Frostline Picket Days
• Contact information for the business
• "Come visit our outdoor showroom, open 24/7!"
Nice to have
• Photos of our fences - you can find more on our website at www.GetBrambleRail.com or Facebook.com/MeadowlarkRailGPV
Should not have
• Flashy designs

```html
<!DOCTYPE html>
<html lang="en">
<head>
<meta charset="utf-8">
<title>Frostline Picket Days – Bramble Rail Fence</title>
<link rel="stylesheet" href="https://fonts.googleapis.com/css2?family=Archivo+Black&family=Arimo:wght@700&family=Fira+Sans:wght@700&display=swap">
<style>
  :root {
    --green: #147a10;
    --ink: #0a0a0a;
    --frame: #5a3310;
    --brand-blue: #4fa8ef;
    --paper: #ffffff;
    --photo-privacy: linear-gradient(160deg, #6e8f4a 0%, #b59c6c 45%, #8a6a3e 100%);
    --photo-split: linear-gradient(180deg, #3f6b2a 0%, #6fae3c 45%, #b79a6c 75%, #7a5a3a 100%);
    --photo-topcap: linear-gradient(160deg, #8fa8b0 0%, #c9b98e 40%, #a58c5e 100%);
  }
  html, body {
    margin: 0;
    padding: 0;
    overflow: hidden;
    background: var(--paper);
  }
  .flyer {
    position: relative;
    width: 857px;
    height: 1200px;
    overflow: hidden;
    background: var(--paper);
    font-family: "Fira Sans", Arial, sans-serif;
    font-weight: 700;
    color: var(--ink);
  }
  .line {
    position: absolute;
    left: 0;
    width: 100%;
    margin: 0;
    text-align: center;
    line-height: 1;
    white-space: nowrap;
  }
  .headline {
    font-family: "Archivo Black", "Arial Black", sans-serif;
    font-weight: 400;
    font-size: 96px;
    color: var(--green);
    letter-spacing: -1px;
    transform: scaleY(1.28);
    transform-origin: center top;
  }
  .headline--top { top: 38px; }
  .headline--bottom { top: 190px; }
  .rule {
    position: absolute;
    left: 39px;
    width: 778px;
    height: 6px;
    background: var(--green);
  }
  .rule--upper { top: 331px; }
  .rule--lower { top: 866px; }
  .price { top: 361px; font-size: 46px; }
  .photo {
    position: absolute;
    top: 430px;
    height: 230px;
    box-sizing: border-box;
    border: 4px solid var(--frame);
  }
  .photo--privacy { left: 31px; width: 219px; background: var(--photo-privacy); }
  .photo--split { left: 279px; width: 302px; background: var(--photo-split); }
  .photo--topcap { left: 612px; width: 218px; background: var(--photo-topcap); }
  .caption {
    position: absolute;
    width: 240px;
    margin: 0;
    font-size: 34px;
    line-height: 1;
    text-align: center;
  }
  .caption--privacy { left: 21px; top: 668px; }
  .caption--split { left: 308px; top: 668px; }
  .caption--topcap { left: 601px; top: 672px; }
  .showroom { top: 732px; font-size: 46px; }
  .hours { top: 779px; font-size: 62px; }
  .brand-name { top: 912px; font-size: 44px; color: var(--brand-blue); }
  .brand-phone { top: 966px; font-size: 42px; }
  .brand-tagline { top: 1022px; font-size: 15px; }
  .website {
    top: 1061px;
    font-family: "Arimo", Arial, sans-serif;
    font-size: 58px;
    letter-spacing: -1px;
  }
  .address { top: 1128px; font-size: 34px; }
</style>
</head>
<body>
  <main class="flyer">
    <h1 class="line headline headline--top">FROSTLINE</h1>
    <p class="line headline headline--bottom">PICKET DAYS</p>
    <div class="rule rule--upper"></div>

    <p class="line price">Wood fences starting at $12/FT</p>

    <div class="photo photo--privacy" role="img" aria-label="Photo of a tall wooden privacy fence lined with rose bushes"></div>
    <div class="photo photo--split" role="img" aria-label="Photo of a wooden split rail fence around a green lawn with a picket gate"></div>
    <div class="photo photo--topcap" role="img" aria-label="Photo of a wooden top cap fence with a hinged gate"></div>

    <p class="caption caption--privacy">Privacy</p>
    <p class="caption caption--split">Split Rail</p>
    <p class="caption caption--topcap">Top Cap</p>

    <p class="line showroom">Come visit our outdoor showroom</p>
    <p class="line hours">-Open 24/7-</p>
    <div class="rule rule--lower"></div>

    <p class="line brand-name">Bramble Rail Fence</p>
    <p class="line brand-phone">704-555-0142</p>
    <p class="line brand-tagline">“Because Good Fences Make Good Neighbors”</p>

    <p class="line website">www.getbramblerail.com</p>
    <p class="line address">436 Quillen Rd. &nbsp;•&nbsp; Monroe, NC 28117</p>
  </main>
</body>
</html>
```